Coralbend Pastoral Traders Business Cards

We require business cards revamped with our logo. A few details we would like to use.

1. Round Edges
2. Our logo over the top of a wagyu cattle background photo on one side of the card

Other side of the card has the below details.

1. Person Name (First & Last)
2. Job Position
3. Mobile Number
4. Email Address
5. Website Address

Simple & Neat.

Target Market(s)

Sales

Industry/Entity Type

Agriculture

Contact Information for Business Card

CORALBEND PASTORAL TRADERS

Colors

Designer to choose colors to be used in the design.

Requirements
Must have
• Company Logo

```html
<!DOCTYPE html>
<html lang="en">
<head>
<meta charset="utf-8">
<title>Coralbend Pastoral Traders – Business Cards</title>
<link rel="stylesheet" href="https://fonts.googleapis.com/css2?family=Cinzel:wght@700&family=Montserrat:wght@400;500&family=Tinos&display=swap">
<style>
  :root {
    --maroon: #6a1523;
    --cattle-red: #7a1818;
    --paper: #ffffff;
    --ink: #2a2226;
    --backdrop: #d9d9d9;
  }
  * { box-sizing: border-box; margin: 0; padding: 0; }
  html, body { width: 1200px; height: 901px; overflow: hidden; }
  body {
    background: var(--backdrop);
    display: flex;
    flex-direction: column;
    align-items: center;
    justify-content: center;
    gap: 44px;
  }
  .card {
    width: 640px;
    height: 366px;
    border-radius: 26px;
    position: relative;
    overflow: hidden;
    box-shadow: 0 10px 28px rgba(0,0,0,.28);
  }

  .brand {
    display: flex;
    align-items: center;
    gap: 16px;
    font-family: "Cinzel", Georgia, serif;
    font-weight: 700;
    line-height: 1.2;
  }
  .brand__dot {
    width: 46px; height: 46px;
    border-radius: 50%;
    flex: none;
  }

  /* Back side */
  .card--back {
    background: var(--maroon);
    display: flex;
    align-items: center;
    justify-content: center;
  }
  .card--back .brand { color: var(--paper); font-size: 30px; letter-spacing: 1px; }
  .card--back .brand__dot { background: var(--paper); }

  /* Front side */
  .card--front { background: var(--paper); }
  .card--front .brand {
    position: absolute;
    left: 42px; top: 46px;
    width: 320px;
    color: var(--maroon);
    font-size: 22px;
    letter-spacing: .5px;
  }
  .card--front .brand__dot { width: 36px; height: 36px; background: var(--maroon); }
  .cattle-art {
    position: absolute;
    right: 30px; top: 60px;
    width: 230px; height: 270px;
    border-radius: 16px;
    background: linear-gradient(160deg, #8a1e1e, var(--cattle-red));
  }
  .holder {
    position: absolute;
    left: 42px; top: 170px;
  }
  .holder__name {
    font-family: "Cinzel", Georgia, serif;
    font-weight: 700;
    font-size: 24px;
    color: var(--maroon);
    letter-spacing: .5px;
  }
  .holder__role {
    font-family: "Montserrat", Arial, sans-serif;
    font-size: 15px;
    color: var(--ink);
    letter-spacing: 1px;
    margin-top: 4px;
  }
  .contacts {
    position: absolute;
    left: 42px; top: 254px;
    list-style: none;
    font-family: "Tinos", "Times New Roman", serif;
    font-size: 16px;
    color: var(--ink);
  }
  .contacts li {
    display: flex;
    align-items: center;
    gap: 10px;
    height: 26px;
  }
  .contacts svg { width: 18px; height: 18px; flex: none; }
</style>
</head>
<body>

  <section class="card card--back">
    <div class="brand"><span class="brand__dot"></span><span>Coralbend Pastoral Traders</span></div>
  </section>

  <section class="card card--front">
    <div class="brand"><span class="brand__dot"></span><span>Coralbend Pastoral Traders</span></div>

    <div class="holder">
      <p class="holder__name">MARCUS HALE</p>
      <p class="holder__role">MANAGING DIRECTOR</p>
    </div>

    <ul class="contacts">
      <li>
        <svg viewBox="0 0 18 18" aria-hidden="true"><rect x="5" y="1.5" width="8" height="15" rx="1.6" fill="none" stroke="#6a1523" stroke-width="1.5"/><line x1="8" y1="14" x2="10" y2="14" stroke="#6a1523" stroke-width="1.5"/></svg>
        044-987 654 321
      </li>
      <li>
        <svg viewBox="0 0 18 18" aria-hidden="true"><rect x="1.5" y="4" width="15" height="10" fill="none" stroke="#6a1523" stroke-width="1.5"/><polyline points="1.5,4 9,10 16.5,4" fill="none" stroke="#6a1523" stroke-width="1.5"/></svg>
        info@coralbend.com
      </li>
      <li>
        <svg viewBox="0 0 18 18" aria-hidden="true"><circle cx="9" cy="9" r="7.5" fill="none" stroke="#6a1523" stroke-width="1.5"/><ellipse cx="9" cy="9" rx="3.2" ry="7.5" fill="none" stroke="#6a1523" stroke-width="1.2"/><line x1="1.5" y1="9" x2="16.5" y2="9" stroke="#6a1523" stroke-width="1.2"/></svg>
        www.coralbendpastoral.com
      </li>
    </ul>

    <div class="cattle-art" role="img" aria-label="Large deep red silhouette of a standing cow"></div>
  </section>

</body>
</html>
```